Stationery for a private security company, "Brennock Security Services Ltd."

Needed is a stationery design for a private security company. The designs must show professionalism and that our company mean nothing but business. Watermark of the company logo on the letterhead page is also a must. The final design must represent innovation and professionalism. It would be great if designers could integrate the colours black and silver onto the cards and letterheads..

Thank you

```html
<!DOCTYPE html>
<html lang="en">
<head>
<meta charset="utf-8">
<title>Brennock Security Services Ltd. — Stationery</title>
<link rel="stylesheet" href="https://fonts.googleapis.com/css2?family=Open+Sans:wght@400;600;700&family=Noto+Serif:wght@400&display=swap">
<style>
  :root{
    --stage:#d9d6d2;
    --paper:#ffffff;
    --ink:#1a1a1a;
    --black:#0d0d0d;
    --silver:#aeb9bd;
    --watermark:#ececec;
  }
  *{box-sizing:border-box;margin:0;padding:0}
  html,body{width:1200px;height:515px;overflow:hidden}
  body{background:var(--stage);position:relative;font-family:"Open Sans",Arial,sans-serif;color:var(--ink)}

  .sheet{position:absolute;top:29px;width:350px;height:453px;background:var(--paper);overflow:hidden;box-shadow:0 1px 4px rgba(0,0,0,.25)}
  .sheet--letter{left:16px}
  .sheet--fax{left:384px}

  .brand{position:absolute;font-family:"Open Sans",Arial,sans-serif;font-weight:700;color:var(--ink);line-height:1;text-transform:uppercase;white-space:nowrap}
  .brand__name{display:block;letter-spacing:.5px}
  .brand__sub{display:block;letter-spacing:.2px}
  .sheet .brand{left:16px;top:28px}
  .sheet .brand__name{font-size:11px}
  .sheet .brand__sub{font-size:4.6px;margin-top:2px}

  .contact{position:absolute;font-family:"Noto Serif",Georgia,serif;font-weight:400;font-size:6.3px;line-height:8.6px;color:var(--ink);list-style:none;white-space:nowrap}
  .sheet .contact{left:234px;top:12px;padding-left:4px;border-left:1px solid #ccc}
  .contact li{display:flex;align-items:center;gap:3px}
  .contact svg{width:5px;height:5px;flex:none}

  .watermark{position:absolute;font-family:"Open Sans",Arial,sans-serif;font-weight:700;color:var(--watermark);text-transform:uppercase;white-space:nowrap;line-height:1}
  .sheet .watermark{left:28px;top:180px;font-size:52px;letter-spacing:2px}

  .footer{position:absolute;left:0;bottom:0;width:100%;height:42px}
  .footer svg{position:absolute;inset:0;width:100%;height:100%}
  .footer__text{position:absolute;left:0;right:0;bottom:7px;text-align:center;font-family:"Noto Serif",Georgia,serif;font-weight:400;font-size:6.6px;color:#e6e6e6;letter-spacing:.4px}

  .fax__title{position:absolute;left:14px;top:100px;font-size:22px;font-weight:400;letter-spacing:.5px}
  .fax__field{position:absolute;font-size:5.6px;border-bottom:1px solid #333;height:10px;line-height:9px}
  .fax__field--l{left:14px;width:169px}
  .fax__field--r{left:191px;width:122px}
  .fax__checks{position:absolute;left:14px;top:222px;width:300px;display:flex;justify-content:space-between;font-size:5.6px}
  .fax__check{display:flex;align-items:center;gap:3px}
  .fax__check::before{content:"";width:7px;height:7px;border:1px solid #444;display:block}

  .option-label{position:absolute;top:486px;font-size:16px;color:#444}

  .envelope{position:absolute;width:392px;height:176px;background:#f4f4f4;overflow:hidden;box-shadow:0 1px 4px rgba(0,0,0,.25)}
  .envelope--back-silver{left:790px;top:30px}
  .envelope--back-black{left:778px;top:106px;height:100px;background:#f0f0f0}
  .envelope__flap{position:absolute;left:0;top:0;width:100%}
  .envelope .watermark{font-size:16px;left:50%;transform:translateX(-50%)}
  .envelope--back-silver .watermark{top:26px;color:#c6cfd2}
  .envelope--back-black .watermark{top:28px;color:#2a2a2a}

  .envelope--front{left:752px;top:194px;height:176px;background:var(--paper)}
  .envelope--front .brand{left:8px;top:26px}
  .envelope--front .brand__name{font-size:9px}
  .envelope--front .brand__sub{font-size:3.8px;margin-top:2px}
  .envelope__address{position:absolute;left:8px;top:46px;font-family:"Noto Serif",Georgia,serif;font-size:5px;line-height:6.5px}
  .envelope--front .watermark{left:178px;top:76px;font-size:34px;transform:none}
  .envelope--front .footer{height:52px}
  .envelope--front .footer__text{font-size:9px;bottom:14px;letter-spacing:.6px}

  .card{position:absolute;width:144px;height:83px;box-shadow:0 1px 4px rgba(0,0,0,.3)}
  .card--front{left:774px;top:400px;background:var(--paper);overflow:hidden}
  .card--front .brand{left:6px;top:38px}
  .card--front .brand__name{font-size:7.6px}
  .card--front .brand__sub{font-size:3.2px;margin-top:1.5px}
  .card--front .contact{left:67px;top:14px;font-size:3.3px;line-height:4.6px;border-left:1px solid #999;padding-left:3px}
  .card--front .contact svg{width:3px;height:3px}
  .card__name{position:absolute;left:0;right:0;bottom:0;height:12px;background:var(--black);color:#ddd;text-align:center;font-size:4.8px;line-height:12px}
  .card__name small{font-size:3.4px;color:#999}
  .card--back{left:934px;top:402px;background:var(--black)}
  .card--back .brand{left:0;right:0;top:30px;text-align:center;color:#cfcfcf}
  .card--back .brand__name{font-size:8.5px}
  .card--back .brand__sub{font-size:3.6px;margin-top:1.5px}
  .card__web{position:absolute;left:0;right:0;top:67px;text-align:center;font-size:4px;color:#777;font-family:"Noto Serif",Georgia,serif}
</style>
</head>
<body>

<svg width="0" height="0" style="position:absolute" aria-hidden="true">
  <defs>
    <symbol id="icon-phone" viewBox="0 0 10 10"><circle cx="5" cy="5" r="5" fill="#1a1a1a"/><path d="M3 2.5l1 1-.6.8a4 4 0 0 0 2.3 2.3l.8-.6 1 1-.8.9C4.8 7.7 2.3 5.2 2.1 3.3z" fill="#fff"/></symbol>
    <symbol id="icon-mail" viewBox="0 0 10 10"><rect x="0" y="2" width="10" height="6.5" fill="#1a1a1a"/></symbol>
    <symbol id="icon-web" viewBox="0 0 10 10"><circle cx="5" cy="5" r="5" fill="#1a1a1a"/></symbol>
  </defs>
</svg>

<section class="sheet sheet--letter" aria-label="Letterhead">
  <div class="brand"><span class="brand__name">Brennock</span><span class="brand__sub">Security Services Ltd.</span></div>
  <ul class="contact">
    <li><svg><use href="#icon-phone"/></svg>123-456-7890</li>
    <li><svg><use href="#icon-phone"/></svg>123-456-7856</li>
    <li><svg><use href="#icon-mail"/></svg>office@brennocksecurity.com</li>
    <li><svg><use href="#icon-web"/></svg>www.brennocksecurity.com</li>
  </ul>
  <div class="watermark" aria-hidden="true">Brennock</div>
  <div class="footer">
    <svg viewBox="0 0 350 42" preserveAspectRatio="none" aria-hidden="true">
      <path d="M0 20 Q175 -2 350 20" fill="none" stroke="var(--silver)" stroke-width="2"/>
      <path d="M0 26 Q175 6 350 26 V42 H0 Z" fill="var(--black)"/>
    </svg>
    <p class="footer__text">Street Name, City Name, State Zipcode</p>
  </div>
</section>
<p class="option-label" style="left:130px">Option-1</p>

<section class="sheet sheet--fax" aria-label="Fax sheet">
  <div class="brand"><span class="brand__name">Brennock</span><span class="brand__sub">Security Services Ltd.</span></div>
  <ul class="contact">
    <li><svg><use href="#icon-phone"/></svg>123-456-7890</li>
    <li><svg><use href="#icon-phone"/></svg>123-456-7856</li>
    <li><svg><use href="#icon-mail"/></svg>office@brennocksecurity.com</li>
    <li><svg><use href="#icon-web"/></svg>www.brennocksecurity.com</li>
  </ul>
  <h1 class="fax__title">FAX</h1>
  <div class="fax__field fax__field--l" style="top:138px">To :</div>
  <div class="fax__field fax__field--r" style="top:138px">From :</div>
  <div class="fax__field fax__field--l" style="top:156px">Fax :</div>
  <div class="fax__field fax__field--r" style="top:156px">Pages :</div>
  <div class="fax__field fax__field--l" style="top:174px">Phone :</div>
  <div class="fax__field fax__field--r" style="top:174px">Date :</div>
  <div class="fax__field fax__field--l" style="top:193px">Re :</div>
  <div class="fax__field fax__field--r" style="top:193px">CC :</div>
  <div class="fax__checks">
    <span class="fax__check">Urgent</span>
    <span class="fax__check">For Review</span>
    <span class="fax__check">Please Comment</span>
    <span class="fax__check">Please Reply</span>
    <span class="fax__check">Please Recycle</span>
  </div>
  <div class="footer">
    <svg viewBox="0 0 350 42" preserveAspectRatio="none" aria-hidden="true">
      <path d="M0 20 Q175 -2 350 20" fill="none" stroke="var(--silver)" stroke-width="2"/>
      <path d="M0 26 Q175 6 350 26 V42 H0 Z" fill="var(--black)"/>
    </svg>
    <p class="footer__text">Street Name, City Name, State Zipcode</p>
  </div>
</section>
<p class="option-label" style="left:523px">Option-2</p>

<section class="envelope envelope--back-silver" aria-label="Envelope back, silver flap">
  <svg class="envelope__flap" viewBox="0 0 392 80" height="80" preserveAspectRatio="none" aria-hidden="true">
    <path d="M0 0 H392 V30 Q392 40 370 46 L230 74 Q196 80 162 74 L22 46 Q0 40 0 30 Z" fill="var(--silver)"/>
  </svg>
  <div class="watermark" aria-hidden="true">Brennock</div>
</section>
<section class="envelope envelope--back-black" aria-label="Envelope back, black flap">
  <svg class="envelope__flap" viewBox="0 0 392 72" height="72" preserveAspectRatio="none" aria-hidden="true">
    <path d="M0 0 H392 V26 Q392 36 370 42 L230 66 Q196 72 162 66 L22 42 Q0 36 0 26 Z" fill="var(--black)"/>
  </svg>
  <div class="watermark" aria-hidden="true">Brennock</div>
</section>

<section class="envelope envelope--front" aria-label="Envelope front">
  <div class="brand"><span class="brand__name">Brennock</span><span class="brand__sub">Security Services Ltd.</span></div>
  <p class="envelope__address">Street Name, City Name<br>State Zipcode</p>
  <div class="watermark" aria-hidden="true">Brennock</div>
  <div class="footer">
    <svg viewBox="0 0 392 52" preserveAspectRatio="none" aria-hidden="true">
      <path d="M0 22 Q196 -2 392 22" fill="none" stroke="var(--silver)" stroke-width="2"/>
      <path d="M0 28 Q196 6 392 28 V52 H0 Z" fill="var(--black)"/>
    </svg>
    <p class="footer__text">www.brennocksecurity.com</p>
  </div>
</section>

<section class="card card--front" aria-label="Business card front">
  <div class="brand"><span class="brand__name">Brennock</span><span class="brand__sub">Security Services Ltd.</span></div>
  <ul class="contact">
    <li>Street Name, City Name</li>
    <li>State Zipcode</li>
    <li><svg><use href="#icon-phone"/></svg>123-456-7890</li>
    <li><svg><use href="#icon-phone"/></svg>123-456-7856</li>
    <li><svg><use href="#icon-mail"/></svg>office@brennocksecurity.com</li>
    <li><svg><use href="#icon-web"/></svg>www.brennocksecurity.com</li>
  </ul>
  <p class="card__name">Your Name, <small>Title</small></p>
</section>
<section class="card card--back" aria-label="Business card back">
  <div class="brand"><span class="brand__name">Brennock</span><span class="brand__sub">Security Services Ltd.</span></div>
  <p class="card__web">www.brennocksecurity.com</p>
</section>

</body>
</html>
```